Tall Oak Grove Transportation Management Association

We are looking to design an awards certificate for an upcoming event that we are having in December. This award would be given to our employee members who have done an outstanding job of promoting commuting alternatives (biking, walking, transit, ridesharing) to driving alone, and as such have reduced green house gas emissions. We are looking for a cool graphic that will make the award something special and worth framing. Attached is our current logo which should be on the certificate somewhere, as well as a few of our program design logos which can be used for inspiration.

Target Market(s)

Board members

Industry/Entity Type

Event

Requirements
Must have
• Graphic suitable for framing as part of an awards certificate
Nice to have
• Something that relates to what we do which is promoting sustainable tranportation (biking, walking, transit, and ridesharing).

```html
<!DOCTYPE html>
<html lang="en">
<head>
<meta charset="utf-8">
<title>Tall Oak Grove TMA – Certificate of Achievement</title>
<link rel="stylesheet" href="https://fonts.googleapis.com/css2?family=Old+Standard+TT:ital,wght@0,400;1,400&family=Carlito&display=swap">
<style>
  :root {
    --paper: #ffffff;
    --ink: #1d1d1d;
    --title-blue: #1a86c4;
    --brand-ink: #2b2522;
    --skin-light: #f6dccd;
    --skin: #e9b9a0;
    --leaf: #8fb86a;
    --leaf-deep: #6e9a4c;
    --globe: #c9dca4;
    --globe-deep: #9fbf72;
    --house-green: #8cc474;
    --ride-red: #ef6a55;
    --bus-blue: #6fb2e0;
    --car-orange: #f5a83a;
    --walk-teal: #5bbfbf;
    --van-olive: #a8b94a;
  }
  * { margin: 0; padding: 0; box-sizing: border-box; }
  html, body { width: 1200px; height: 927px; overflow: hidden; background: var(--paper); }
  .certificate {
    position: relative;
    width: 1200px; height: 927px;
    background: var(--paper);
    color: var(--ink);
    font-family: "Old Standard TT", "Times New Roman", serif;
    overflow: hidden;
  }
  .hero-photo { position: absolute; inset: 0; }
  .hero-photo svg { display: block; }

  .brand {
    position: absolute; left: 0; right: 0; top: 50px;
    text-align: center; color: var(--brand-ink);
  }
  .brand-name { font-size: 40px; line-height: 46px; }
  .brand-sub { font-size: 14px; line-height: 22px; letter-spacing: 0.5px; }

  .title {
    position: absolute; left: 0; right: 0; top: 158px;
    text-align: center; font-style: italic; font-weight: 400;
    font-size: 77px; line-height: 92px; color: var(--title-blue);
  }
  .line { position: absolute; left: 0; right: 0; text-align: center; font-style: italic; }
  .awarded { top: 261px; font-size: 25px; }
  .recipient-rule {
    position: absolute; left: 115px; width: 965px; top: 361px;
    border-top: 1.5px dotted #555;
  }
  .citation { top: 396px; font-size: 23.5px; line-height: 30px; }
  .date-line { top: 482px; font-size: 25px; }
  .place-line { top: 533px; font-size: 25px; }

  .sign-field {
    position: absolute; top: 672px;
    font-family: "Carlito", Calibri, sans-serif; font-size: 22px;
  }
  .accredited { left: 209px; }
  .signature { left: 681px; }

  .programs { position: absolute; left: 0; right: 0; top: 745px; height: 130px; }
  .program-art { position: absolute; top: 0; height: 88px; border-radius: 10px; }
  .program-path {
    position: absolute; left: 55px; width: 1075px; top: 80px; height: 3px; border-radius: 2px;
    background: linear-gradient(90deg, var(--house-green) 0 17%, var(--ride-red) 17% 36%, var(--bus-blue) 36% 53%, var(--car-orange) 53% 65%, var(--walk-teal) 65% 80%, var(--van-olive) 80% 100%);
  }
  .program-label {
    position: absolute; top: 105px;
    font-family: "Carlito", Calibri, sans-serif; font-size: 17px; color: var(--ink);
    white-space: nowrap;
  }
</style>
</head>
<body>
<main class="certificate">
  <div class="hero-photo" role="img" aria-label="Soft photo of cupped hands holding a small green globe in front of a maple leaf">
    <svg width="1200" height="927" viewBox="0 0 1200 927" aria-hidden="true">
      <defs>
        <radialGradient id="leafGlow" cx="0.5" cy="0.5" r="0.5">
          <stop offset="0" stop-color="var(--leaf-deep)" stop-opacity="0.55"/>
          <stop offset="0.6" stop-color="var(--leaf)" stop-opacity="0.3"/>
          <stop offset="1" stop-color="var(--leaf)" stop-opacity="0"/>
        </radialGradient>
        <radialGradient id="globeGlow" cx="0.45" cy="0.4" r="0.55">
          <stop offset="0" stop-color="var(--globe)" stop-opacity="0.9"/>
          <stop offset="0.75" stop-color="var(--globe-deep)" stop-opacity="0.65"/>
          <stop offset="1" stop-color="var(--globe-deep)" stop-opacity="0"/>
        </radialGradient>
        <radialGradient id="skinGlow" cx="0.5" cy="0.5" r="0.5">
          <stop offset="0" stop-color="var(--skin)" stop-opacity="0.55"/>
          <stop offset="0.7" stop-color="var(--skin-light)" stop-opacity="0.35"/>
          <stop offset="1" stop-color="var(--skin-light)" stop-opacity="0"/>
        </radialGradient>
        <linearGradient id="fadeTop" x1="0" y1="0" x2="0" y2="1">
          <stop offset="0" stop-color="#fff" stop-opacity="0.85"/>
          <stop offset="0.3" stop-color="#fff" stop-opacity="0.35"/>
          <stop offset="1" stop-color="#fff" stop-opacity="0"/>
        </linearGradient>
      </defs>
      <ellipse cx="860" cy="310" rx="270" ry="260" fill="url(#leafGlow)"/>
      <ellipse cx="330" cy="330" rx="420" ry="150" fill="url(#skinGlow)"/>
      <ellipse cx="700" cy="560" rx="480" ry="190" fill="url(#skinGlow)"/>
      <ellipse cx="950" cy="520" rx="200" ry="150" fill="url(#skinGlow)"/>
      <circle cx="820" cy="420" r="180" fill="url(#globeGlow)"/>
      <rect x="0" y="0" width="1200" height="360" fill="url(#fadeTop)"/>
    </svg>
  </div>

  <header class="brand">
    <div class="brand-name">Tall Oak Grove TMA</div>
    <div class="brand-sub">Tall Oak Grove Transportation Management Association</div>
  </header>

  <h1 class="title">Certificate of Achievement</h1>
  <p class="line awarded">This Certilficate is awarded to</p>
  <div class="recipient-rule"></div>
  <p class="line citation">For doing outstanding job of promoting Community Alternatives (biking, walking, transit and ridesharing)<br>Thus reducing green house gas emmissions</p>
  <p class="line date-line">On this................................day of................December, 2015</p>
  <p class="line place-line">At................................Given by.......................................</p>

  <p class="sign-field accredited">Accredited by................................</p>
  <p class="sign-field signature">Signature................................</p>

  <section class="programs">
    <div class="program-art" style="left:60px;width:165px;background:linear-gradient(180deg,rgba(140,196,116,0.12),rgba(140,196,116,0.4))" role="img" aria-label="Line drawing of a house and a car for Guaranteed Ride Home"></div>
    <div class="program-art" style="left:232px;width:182px;background:linear-gradient(180deg,rgba(239,106,85,0.1),rgba(239,106,85,0.38))" role="img" aria-label="Line drawing of a car with riders between two houses for Ride Matching"></div>
    <div class="program-art" style="left:448px;width:150px;background:linear-gradient(180deg,rgba(111,178,224,0.12),rgba(111,178,224,0.42))" role="img" aria-label="Line drawing of a bus and a ferry for Express Yourself"></div>
    <div class="program-art" style="left:618px;width:140px;background:linear-gradient(180deg,rgba(245,168,58,0.12),rgba(245,168,58,0.42))" role="img" aria-label="Line drawing of a carpool car with passengers for Carpool Subsidy"></div>
    <div class="program-art" style="left:768px;width:132px;background:linear-gradient(180deg,rgba(91,191,191,0.12),rgba(91,191,191,0.42))" role="img" aria-label="Line drawing of a walker and a cyclist for Workout to Work"></div>
    <div class="program-art" style="left:960px;width:170px;background:linear-gradient(180deg,rgba(168,185,74,0.12),rgba(168,185,74,0.42))" role="img" aria-label="Line drawing of a van for Vanpool Subsidy"></div>
    <div class="program-path"></div>

    <span class="program-label" style="left:53px">Guaranteed Ride Home</span>
    <span class="program-label" style="left:266px">Ride Matching</span>
    <span class="program-label" style="left:448px">Express Yourself</span>
    <span class="program-label" style="left:624px">Carpool Subsidy</span>
    <span class="program-label" style="left:783px">Workout to Work</span>
    <span class="program-label" style="left:967px">Vanpool Subsidy</span>
  </section>
</main>
</body>
</html>
```